Mini-Banner für Rubriken
Hallo,
wir benötigen für unsere Seite www.velmaro.de neue und vorallem passende Banner für die Highlights (rechte Seite) innerhalb der Rubriken, wie z.B. All Inklusive, Wellness, Urlaub an der Küste u.s.w. Vielen Dank für die Vorschläge !

```html
<!DOCTYPE html>
<html lang="de">
<head>
<meta charset="utf-8">
<title>velmaro – Highlights</title>
<link href="https://fonts.googleapis.com/css2?family=PT+Sans:wght@400;700&family=Open+Sans:ital,wght@1,800&family=Merriweather+Sans:ital,wght@1,500&display=swap" rel="stylesheet">
<style>
  :root{
    --sky:#2f8ee0;
    --sky-light:#cfe6f8;
    --orange:#f39a1e;
    --green:#8cc63f;
    --panel:#efeeee;
    --panel-line:#c9c9c9;
    --text:#222;
    --muted:#8a8a8a;
    --accent-red:#c98a7a;
  }
  *{margin:0;padding:0;box-sizing:border-box}
  html,body{width:838px;height:1200px;overflow:hidden}
  body{position:relative;background:#fff;font-family:"PT Sans",Tahoma,sans-serif;color:var(--text)}
  .edge-band{position:absolute;top:0;right:0;width:80px;height:1200px;background:linear-gradient(90deg,#5aa7e8,var(--sky) 40%,#1f7fd4)}
  .top-band{position:absolute;top:0;left:0;width:838px;height:60px;background:linear-gradient(90deg,#ffffff 0%,#e8f3fc 55%,var(--sky) 100%)}
  .header{position:absolute;top:40px;left:0;width:750px;height:305px;background:#fff;border-radius:0 40px 0 0;overflow:hidden}
  .header-photo{position:absolute;top:0;left:260px;width:490px;height:305px;background:linear-gradient(160deg,#9cc9ee 0%,#dfeaf4 45%,#f2f4f6 70%,#c9d4de 100%)}
  .header-fade{position:absolute;top:0;left:0;width:420px;height:305px;background:linear-gradient(90deg,#fff 55%,rgba(255,255,255,0))}
  .header-kicker{position:absolute;top:70px;left:-20px;font-family:"Open Sans",sans-serif;font-style:italic;font-weight:800;font-size:62px;color:var(--sky-light);letter-spacing:1px}
  .header-title{position:absolute;top:150px;left:-14px;font-family:"Open Sans",sans-serif;font-style:italic;font-weight:800;font-size:70px;color:var(--orange)}
  .header-nav{position:absolute;top:246px;left:0;width:560px;height:38px;background:linear-gradient(90deg,#b6dd7d,var(--green));border-radius:0 0 30px 0;color:#fff;font-size:24px;line-height:38px;padding-left:14px;font-weight:700}
  .content{position:absolute;top:368px;left:-10px;width:210px;height:620px;border:3px dotted #cfcfcf;border-left:none}
  .content-label{position:absolute;left:0;font-size:31px;font-weight:700;color:var(--accent-red);text-align:right}
  .label-a{top:40px;width:22px;overflow:hidden}
  .label-b{top:78px;width:212px;overflow:hidden;white-space:nowrap;direction:rtl}
  .content-photo{position:absolute;top:160px;left:0;width:98px;height:345px;border-radius:0 14px 14px 0;background:linear-gradient(180deg,#e9e2dc,#c9b5a6 60%,#d8cfc6)}
  .content-rule{position:absolute;top:562px;left:0;width:180px;border-top:3px solid #cfcfcf}
  .content-text{position:absolute;top:1105px;left:0;font-size:29px;line-height:42px;color:var(--muted);white-space:nowrap}
  .box{position:absolute;left:238px;width:498px;background:var(--panel);border:2px solid var(--panel-line);border-radius:12px;box-shadow:2px 3px 4px rgba(0,0,0,.25)}
  .highlights{top:378px;height:590px}
  .box-head{height:62px;line-height:62px;text-align:center;font-weight:700;font-size:29px;border-bottom:2px solid var(--panel-line)}
  .teaser{position:absolute;left:8px;width:480px;height:155px;border-bottom:3px solid #8b8b8b;overflow:hidden}
  .teaser-photo{position:absolute;inset:0}
  .teaser-title{position:absolute;font-family:"Merriweather Sans",sans-serif;font-style:italic;font-weight:500;font-size:38px;line-height:42px;color:#fff;text-shadow:1px 2px 3px rgba(0,0,0,.55)}
  .teaser-wellness{top:76px}
  .teaser-wellness .teaser-photo{background:linear-gradient(180deg,#7fb1e0 0%,#b9d6ef 55%,#7d8fa0 75%,#5d7a8c 100%)}
  .teaser-wellness .teaser-title{top:38px;right:22px;text-align:center}
  .teaser-inclusive{top:242px}
  .teaser-inclusive .teaser-photo{background:linear-gradient(90deg,#f6ead2 0%,#e6c792 45%,#b27a44 100%)}
  .teaser-inclusive .teaser-title{top:30px;right:18px;text-align:right}
  .teaser-harz{top:414px}
  .teaser-harz .teaser-photo{background:linear-gradient(90deg,#3e5566 0%,#6f8796 55%,#e9b34a 80%,#f3f0e6 100%)}
  .teaser-harz .teaser-title{top:36px;left:18px}
  .support{top:1000px;height:240px;background:#fff}
  .support .box-head{background:var(--panel);border-radius:10px 10px 0 0;font-size:30px}
  .support-text{padding:18px 20px;font-size:31px;line-height:38px}
</style>
</head>
<body>
  <div class="edge-band"></div>
  <div class="top-band"></div>

  <header class="header">
    <div class="header-photo" role="img" aria-label="Winterurlaub: Kinder mit Mützen im Schnee vor Bergkulisse"></div>
    <div class="header-fade"></div>
    <div class="header-kicker">reisen...</div>
    <div class="header-title">Specials</div>
    <nav class="header-nav">&nbsp;AGB</nav>
  </header>

  <section class="content">
    <div class="content-label label-a">k</div>
    <div class="content-label label-b">Getränke</div>
    <div class="content-photo" role="img" aria-label="Hotelzimmer mit Einrichtung"></div>
    <div class="content-rule"></div>
  </section>
  <div class="content-text" style="left:-70px">Einfach - im<br>telefonisch</div>

  <aside class="box highlights">
    <div class="box-head">Highlights</div>
    <a class="teaser teaser-wellness">
      <div class="teaser-photo" role="img" aria-label="Bergpanorama in Bayern unter blauem Himmel"></div>
      <div class="teaser-title">Wellnessurlaub<br>in Bayern</div>
    </a>
    <a class="teaser teaser-inclusive">
      <div class="teaser-photo" role="img" aria-label="Gedeckter Tisch mit Gebäck und Speisen"></div>
      <div class="teaser-title">All Inclusive<br>im Erzgebirge</div>
    </a>
    <a class="teaser teaser-harz">
      <div class="teaser-photo" role="img" aria-label="Felsen am Wasser mit gelben und weißen Blüten"></div>
      <div class="teaser-title">Erholungsurlaub<br>im Harz</div>
    </a>
  </aside>

  <aside class="box support">
    <div class="box-head">velmaro Telefon Support</div>
    <p class="support-text">Sie möchten dieses Angebot telefonisch buchen oder wünschen eine persönliche</p>
  </aside>
</body>
</html>
```